International Property Consultancy

Brief Overview:

I need a dynamic and well designed website that is easy to use and understand. It has to be unique and different to generic templates that most websites seem to be these days. PLEASE NO GENERIC TEMPLATES FROM THE INTERNET.

Our business has 10 years experience working on struggling international developments that we then work in-house for to turn around and brings bout success. We stay within a project often for long periods of time until success is achieved. We are unique in our approach and completely different to the standard routes to market for many developments. The site is for developers to see what we have done in regards to previous projects, as such we want to incorporate video into this site with a strong design aesthetic. There will be videos of the past projects we have worked on, which will act as case studies.

I like very simple but punchy websites, that people can navigate and understand very easily. Also a big fan of unique and well thought out design aesthetic.

Initial Site layout thoughts:

1) Homepage:
2) About Us
3) What we've done / Work
This part has the projects we have worked on (France, Portugal, London, Morocco). Each one will have some video content and photo images, but also would be good to have a succinct way to mention what we did and the successes in a clever and punchy way.

4) Contact Us

* This is just a guideline. Would be open to input and creative direction on your own part.

*More details and websites we like can be seen in the brief doc attached.

PLEASE VIEW THE WIREFRAME WORD DOC ATTACHED.

Here there are also some more examples to help:

Here are just a few examples of websites and what I like about them:

- www.velmoro.com (clean, nice geometric design aesthetic, good animation when loading and changing pages well thought out all though also coulee be considered a bit dull and basic after the initial homepage slide)
- https://www.farbridgehub.net (Clean site, quite clinical, lacks video content and doesn't engage greatly).
- https://ruskotile.com (minimal, and like how it mixes the design aesthetic more with video and photo content)

- https://www.amberquillworks.com (like the layout of this and how it displays the projects and work section)

- https://brisk.com (Good use of video content)

- https://loomfield.studio (minimal to the point and mixes design with video and animation etc...)

Here is another couple of cool websites that may help give you some direction: https://halvenquay.com www.brisk.com

Hi there, One of the things I thought would be good on the homepage is to add the logo with a 'digital landscape' before flicking down into a slide with video content of the projects... Just an idea but have posted some pics in the brief. We would get this animated for the site. But if you have better ideas, please do run with them. Thanks,

Target Market(s)

Property developers

Number of Pages Required

4 page

Font styles to use
Other font styles liked:
• Read brief

Requirements
Must have
• Needs to be clean, dynamic and easy to follow on desktop and mobile. We will use it as a kind of portfolio website so will need to embed video of past projects we have worked on.

Read brief in docs.
Nice to have
• Clean
Should not have
• Not be another generic template website.
Not have random property stock photos. (We are not a property agency).

```html
<!DOCTYPE html>
<html lang="en">
<head>
<meta charset="utf-8">
<title>Corvanta — International Property Developments</title>
<link rel="stylesheet" href="https://fonts.googleapis.com/css2?family=Montserrat:wght@400;500;600;700&display=swap">
<style>
  :root {
    --ink: #0e4256;
    --logo-ink: #231f20;
    --hero-bg: #f4f7fa;
    --blush: #f8e1da;
    --accent: #fc5a24;
    --muted: #666b70;
    --footer-bg: #f4f4f4;
    --rule: #dcdcdc;
    --menu: #1b5fa8;
  }
  * { box-sizing: border-box; margin: 0; padding: 0; }
  html, body { width: 755px; height: 1200px; overflow: hidden; }
  body { font-family: "Montserrat", sans-serif; background: #fff; position: relative; color: var(--ink); }
  .brand { font-family: "Montserrat", sans-serif; font-weight: 500; color: var(--logo-ink); letter-spacing: -0.5px; }

  .hero { position: absolute; left: 0; top: 0; width: 755px; height: 358px; background: var(--hero-bg); overflow: hidden; }
  .hero .brand { position: absolute; left: 62px; top: 6px; font-size: 19px; }
  .menu-toggle { position: absolute; left: 677px; top: 12px; }
  .hero-photo { position: absolute; left: 420px; top: 0; width: 335px; height: 358px;
    background: linear-gradient(160deg, #eef2f5 0%, #d9dfe6 45%, #1f3656 100%); }
  .idea-mark { position: absolute; left: 82px; top: 112px; width: 14px; height: 28px; border-radius: 7px 7px 3px 3px; background: var(--accent); }
  .eyebrow { position: absolute; left: 80px; top: 154px; font-size: 12.5px; font-weight: 500; letter-spacing: 5.5px; color: var(--logo-ink); }
  .hero h1 { position: absolute; left: 80px; top: 175px; font-size: 26.5px; line-height: 31px; font-weight: 700; color: var(--ink); }

  .intro { position: absolute; left: 0; top: 358px; width: 755px; height: 289px; background: var(--blush); }
  .intro-flourish { position: absolute; left: 325px; top: 77px; width: 105px; height: 35px; border-radius: 18px; background: rgba(35,31,32,0.08); }
  .intro .brand { position: absolute; left: 0; width: 755px; top: 100px; text-align: center; font-size: 50px; font-weight: 600; }
  .tagline { position: absolute; left: 0; width: 755px; top: 160px; text-align: center; font-size: 10px; color: #4a4a4a; }
  .play { position: absolute; left: 63px; top: 198px; width: 60px; height: 60px; border-radius: 50%; background: #fff; box-shadow: 0 6px 16px rgba(200,150,140,0.35); display: flex; align-items: center; justify-content: center; }

  .success { position: absolute; left: 0; top: 647px; width: 755px; height: 419px; }
  .big-number { position: absolute; left: 60px; top: 113px; font-size: 70px; line-height: 70px; font-weight: 500; color: var(--blush); letter-spacing: -4px; }
  .success h2 { position: absolute; left: 126px; top: 130px; font-size: 22px; line-height: 24px; font-weight: 700; }
  .success p { position: absolute; left: 74px; top: 200px; width: 320px; font-size: 11.8px; line-height: 17px; color: var(--muted); }
  .cta { position: absolute; left: 80px; top: 252px; width: 124px; height: 32px; background: var(--accent); color: #fff; font-size: 10.5px; font-weight: 500; display: flex; align-items: center; justify-content: center; text-decoration: none; }
  .success-art { position: absolute; left: 440px; top: 48px; width: 260px; height: 290px; border-radius: 6px;
    background: linear-gradient(180deg, #e7ecf6 0%, #c9cde6 60%, #f4f4f6 100%); }

  .site-footer { position: absolute; left: 0; top: 1066px; width: 755px; height: 134px; background: var(--footer-bg); }
  .site-footer .brand { position: absolute; left: 0; width: 755px; top: 32px; text-align: center; font-size: 16px; }
  .footer-nav { position: absolute; left: 0; width: 755px; top: 70px; display: flex; justify-content: center; gap: 11px; font-size: 8px; color: #555; }
  .footer-nav span.sep { color: #777; }
  .footer-rule { position: absolute; left: 62px; top: 103px; width: 631px; height: 1px; background: var(--rule); }
  .copyright { position: absolute; left: 62px; top: 110px; font-size: 7.5px; color: #666; }
  .social { position: absolute; left: 617px; top: 108px; display: flex; gap: 10px; }
  .social span { width: 11px; height: 11px; border-radius: 2px; background: #3a6fb5; display: block; }
  .social span:nth-child(2) { background: var(--accent); }
</style>
</head>
<body>
  <header class="hero">
    <div class="hero-photo" role="img" aria-label="Photo of a consultant in a navy blazer holding a clipboard"></div>
    <div class="brand">corvanta.</div>
    <svg class="menu-toggle" width="16" height="12" viewBox="0 0 16 12" aria-label="Menu">
      <rect x="4" y="0" width="12" height="1.6" fill="var(--menu)"/>
      <rect x="0" y="5" width="16" height="1.6" fill="var(--menu)"/>
      <rect x="6" y="10" width="10" height="1.6" fill="var(--menu)"/>
    </svg>
    <div class="idea-mark" role="img" aria-label="Light bulb icon"></div>
    <div class="eyebrow">WE ARE CORVANTA</div>
    <h1>We Fulfill International<br>Property Developments</h1>
  </header>

  <section class="intro">
    <div class="intro-flourish" role="img" aria-label="Hand-drawn line flourish"></div>
    <div class="brand">corvanta.</div>
    <div class="tagline">FINDING PROPERTY BUSINESS SOLUTIONS</div>
    <a class="play" aria-label="Play video">
      <svg width="8" height="9" viewBox="0 0 8 9"><path d="M0 0 L8 4.5 L0 9Z" fill="#111"/></svg>
    </a>
  </section>

  <section class="success">
    <div class="big-number">10</div>
    <h2>YEARS OF SUCCESS<br>AROUND THE WORLD</h2>
    <p>We deliver a unique and truly bespoke approach to delivering international developments to market</p>
    <a class="cta" href="#work">SEE OUR WORK</a>
    <div class="success-art" role="img" aria-label="Illustration of a presentation easel with a bar chart and target icons"></div>
  </section>

  <footer class="site-footer">
    <div class="brand">corvanta.</div>
    <nav class="footer-nav">
      <span>HOME</span><span class="sep">I</span>
      <span>ABOUT US</span><span class="sep">I</span>
      <span>OUR WORK</span><span class="sep">I</span>
      <span>CONTACFT US</span>
    </nav>
    <div class="footer-rule"></div>
    <div class="copyright">COPYRIGHT © 2020 COMPANY ALL RIGHTS RESERVED.</div>
    <div class="social" aria-label="Social links">
      <span></span><span></span><span></span><span></span>
    </div>
  </footer>
</body>
</html>
```